Business Card Design Project

We are not a new company, but renamed to "Norvane Kitchens" last year. We specialize in modern high-end cabinetry imports. We would like to communicate a sense of quality and cutting edge technology. Ideally the design would incorporate our logo colors, silver, red and preferably a black, matte background. Though we are open to suggestions.
Logo is attached.
Edit: I have attached rough drafts of the previous cards, this way you will have all necessary content that needs to go on the cards.
Updates
Project Deadline Extended
Reason: We have received a lot of great designs, but due to the sheer number we couldn't respond to all. We will extend the deadline for another 7 days to finalize and provide feedback to designers.
Thank you for your hard work!
Industry/Entity Type
Business
Look and feel
Each slider illustrates characteristics of the customer's brand and the style your logo design should communicate.

```html
<!DOCTYPE html>
<html lang="en">
<head>
<meta charset="utf-8">
<title>Norvane Kitchens – Business Cards</title>
<link rel="stylesheet" href="https://fonts.googleapis.com/css2?family=Open+Sans:wght@400;600&display=swap">
<style>
  :root {
    --backdrop: #d8b88a;
    --card-cream: #fdfcef;
    --card-black: #0d0d0d;
    --card-black-soft: #2a2a2a;
    --ink: #1a1a1a;
    --brand-red: #e0201a;
    --silver: #c4c4c4;
    --graphite: #5e5e5e;
    --shadow: rgba(40, 25, 10, 0.35);
  }
  * { margin: 0; padding: 0; box-sizing: border-box; }
  html, body {
    width: 1200px; height: 901px; overflow: hidden;
    background: var(--backdrop);
    font-family: "Open Sans", Arial, sans-serif;
  }
  .sheet { position: relative; width: 1200px; height: 901px; }

  .masthead {
    position: absolute; left: 0; top: 70px; width: 1200px;
    display: flex; flex-direction: column; align-items: center; gap: 22px;
  }
  .masthead .mark {
    width: 64px; height: 64px; background: var(--graphite);
  }
  .masthead .wordmark {
    font-size: 34px; font-weight: 600; letter-spacing: 3px;
    color: var(--graphite); text-transform: uppercase;
  }

  .card {
    position: absolute; width: 527px; height: 265px;
    box-shadow: 0 4px 10px var(--shadow);
    overflow: hidden;
  }
  .card.left  { left: 56px; }
  .card.right { left: 617px; }
  .card.front { top: 276px; background: var(--card-cream); }
  .card.back  {
    top: 572px;
    background: linear-gradient(to bottom, var(--card-black) 0%, var(--card-black) 55%, var(--card-black-soft) 100%);
  }

  .front .band { position: absolute; left: 0; top: 0; }
  .front .brand {
    position: absolute; right: 18px; top: 28px;
    display: flex; align-items: center; gap: 10px;
  }
  .front .brand .mark { width: 18px; height: 18px; background: var(--silver); }
  .front .brand .wordmark {
    font-size: 18px; font-weight: 600; letter-spacing: 1.5px;
    color: var(--silver); text-transform: uppercase;
  }

  .person {
    position: absolute; left: 14px; top: 110px; width: 230px;
  }
  .person .name {
    font-size: 19px; font-weight: 400; color: var(--brand-red);
    text-transform: uppercase; line-height: 1.1;
  }
  .person .role {
    font-size: 17px; color: var(--ink); text-align: right;
    margin-top: 4px;
  }
  .divider {
    position: absolute; left: 254px; top: 117px; width: 2px; height: 129px;
    background: var(--brand-red);
  }
  .contact {
    position: absolute; left: 272px; top: 111px;
    font-size: 13px; color: var(--ink); line-height: 22px;
    list-style: none;
  }
  .contact li { display: flex; }
  .contact .label { width: 24px; }
  .contact .indent { padding-left: 24px; }

  .back .brand {
    position: absolute; inset: 0;
    display: flex; flex-direction: column; align-items: center; justify-content: center; gap: 26px;
  }
  .back .brand .mark { width: 60px; height: 60px; background: var(--graphite); }
  .back .brand .wordmark {
    font-size: 34px; font-weight: 600; letter-spacing: 3px;
    color: var(--silver); text-transform: uppercase;
  }
</style>
</head>
<body>
<main class="sheet">

  <header class="masthead">
    <div class="mark"></div>
    <div class="wordmark">Norvane Kitchens</div>
  </header>

  <section class="card front left">
    <svg class="band" width="527" height="265" viewBox="0 0 527 265">
      <rect x="0" y="0" width="527" height="98" fill="#0d0d0d"/>
      <path d="M0 0 H338 C300 0 292 20 284 50 C276 80 262 92 240 92 H0 Z" fill="#fdfcef"/>
    </svg>
    <div class="brand"><span class="mark"></span><span class="wordmark">Norvane Kitchens</span></div>
    <div class="person">
      <div class="name">Adrian Kovel</div>
      <div class="role">Director</div>
    </div>
    <div class="divider"></div>
    <ul class="contact">
      <li><span class="label">p</span>780.555.0142</li>
      <li><span class="label">f</span>780.555.0187</li>
      <li><span class="label">c</span>780.555.0163</li>
      <li><span class="label">@</span>adrian@norvanekitchens.ca</li>
      <li><span class="label">a</span>4120 - 87 St.</li>
      <li class="indent">Edmonton, AB T5X 2K4</li>
    </ul>
  </section>

  <section class="card front right">
    <svg class="band" width="527" height="265" viewBox="0 0 527 265">
      <rect x="0" y="0" width="527" height="98" fill="#0d0d0d"/>
      <path d="M0 0 H338 C300 0 292 20 284 50 C276 80 262 92 240 92 H0 Z" fill="#fdfcef"/>
    </svg>
    <div class="brand"><span class="mark"></span><span class="wordmark">Norvane Kitchens</span></div>
    <div class="person">
      <div class="name">Victor Kovel</div>
      <div class="role">President</div>
    </div>
    <div class="divider"></div>
    <ul class="contact">
      <li><span class="label">p</span>780.555.0142</li>
      <li><span class="label">f</span>780.555.0187</li>
      <li><span class="label">c</span>780.555.0129</li>
      <li><span class="label">@</span>victor@norvanekitchens.ca</li>
      <li><span class="label">a</span>4120 - 87 St.</li>
      <li class="indent">Edmonton, AB T5X 2K4</li>
    </ul>
  </section>

  <section class="card back left">
    <div class="brand"><span class="mark"></span><span class="wordmark">Norvane Kitchens</span></div>
  </section>

  <section class="card back right">
    <div class="brand"><span class="mark"></span><span class="wordmark">Norvane Kitchens</span></div>
  </section>

</main>
</body>
</html>
```